Inflatable Movie Screen company needs a Brochure Design for sales kit

We need a brochure as per attached sketch drawing which is to:
1)follow the sample layout
2) attached images must be used
3) to follow company corporate colors or suggest something professional and appropriate for the theme
Updates

Target Market(s)

Corporate and Community Clubs

Industry/Entity Type

Entertainment

Requirements
Must have
• Colors to be in line with corporate colors OR to suggest something appropriate.
Nice to have
• A unique concept
Should not have
• Too fanciful

```html
<!DOCTYPE html>
<html lang="en">
<head>
<meta charset="utf-8">
<title>Lumora — Inflatable Movie Screening Brochure</title>
<link href="https://fonts.googleapis.com/css2?family=Cinzel:wght@400;700&display=swap" rel="stylesheet">
<style>
  :root {
    --backdrop: #ece8e1;
    --page: #939397;
    --page-shade: #838386;
    --ink: #ffffff;
    --ring: #ffffff;
    --night-top: #1a2138;
    --night-bottom: #0d0c0b;
    --screen-glow: #a88a62;
  }
  * { margin: 0; padding: 0; box-sizing: border-box; }
  html, body { width: 1200px; height: 1200px; overflow: hidden; }
  body { background: var(--backdrop); font-family: "Cinzel", serif; color: var(--ink); }

  .spread { position: absolute; left: 20px; top: 190px; width: 1160px; height: 819px; }
  .spread-art { position: absolute; inset: 0; }

  .brand {
    position: absolute; left: 734px; top: 38px; width: 271px; height: 105px;
    display: flex; flex-direction: column; align-items: center; justify-content: center;
  }
  .brand-name { font-size: 42px; font-weight: 400; letter-spacing: 1px; line-height: 1; }
  .brand-legal { font-size: 8px; font-weight: 400; letter-spacing: 1px; margin-top: 6px; }

  .title {
    position: absolute; right: 49px; top: 158px; width: 560px; text-align: right;
    font-size: 29px; font-weight: 700; letter-spacing: 1px; white-space: nowrap;
  }

  .epigraph {
    position: absolute; right: 40px; top: 236px; width: 460px; text-align: right;
    font-size: 16.5px; line-height: 24.5px; font-weight: 400; letter-spacing: 0.5px;
    white-space: nowrap;
  }
  .epigraph cite { font-style: normal; font-weight: 700; display: block; }

  .testimonial {
    position: absolute; left: 618px; top: 676px; width: 400px;
    font-size: 13.5px; line-height: 20.5px; letter-spacing: 0.4px; white-space: nowrap;
  }
</style>
</head>
<body>
  <section class="spread">
    <svg class="spread-art" width="1160" height="819" viewBox="0 0 1160 819">
      <defs>
        <linearGradient id="fold-shade" x1="0" x2="1" y1="0" y2="0">
          <stop offset="0" stop-color="var(--page)"/>
          <stop offset="0.55" stop-color="var(--page)"/>
          <stop offset="1" stop-color="var(--page-shade)"/>
        </linearGradient>
        <radialGradient id="night-scene" cx="0.55" cy="0.45" r="0.6">
          <stop offset="0" stop-color="var(--screen-glow)"/>
          <stop offset="0.35" stop-color="#3a3330"/>
          <stop offset="0.7" stop-color="var(--night-top)"/>
          <stop offset="1" stop-color="var(--night-bottom)"/>
        </radialGradient>
        <clipPath id="page-clip"><rect width="1160" height="819"/></clipPath>
      </defs>
      <rect class="page-left" x="0" y="0" width="580" height="819" fill="url(#fold-shade)"/>
      <rect class="page-right" x="580" y="0" width="580" height="819" fill="var(--page)"/>
      <g clip-path="url(#page-clip)">
        <circle class="photo-ring" cx="580" cy="755" r="468" fill="var(--ring)"/>
        <circle class="photo" cx="580" cy="755" r="459" fill="url(#night-scene)"
                role="img" aria-label="Night photo of an inflatable outdoor movie screen lit up in a park among trees"/>
      </g>
    </svg>

    <div class="brand">
      <div class="brand-name">LUMORA</div>
      <div class="brand-legal">LUMORA EVENTS PTE LTD</div>
    </div>

    <h1 class="title">Inflatable Movie Screening</h1>

    <blockquote class="epigraph">
      Off all our inventions for mass<br>
      communication, pictures still speak<br>
      the most universally<br>
      understood language.
      <cite>- Arthur Penrose</cite>
    </blockquote>

    <blockquote class="testimonial">
      “Enjoyed wateking &lt;move name&gt; with<br>
      my family. It was nice to get away<br>
      from the usual malls and bond<br>
      together. My kids loved it!”<br>
      - Mei Tan, housewife
    </blockquote>
  </section>
</body>
</html>
```